Layout of a white paper from an already written word document

We are a consulting company specializing in General Data Protection Regulation (GDPR) and cybersecurity. We wish to publish a white paper on our methodologies. The text is ready and we would like it to be laid out in a neat design.
Our target is SMEs and mid-caps.
We try to provide very concrete and pragmatic solutions to our clients. Attached is a sample white paper that we appreciate and the text to format.
Our web site: www.marlow-vantage.net
Target Market(s)
SMEs and mid-caps
Requirements
Must have
- A4 Format

```html
<!DOCTYPE html>
<html lang="fr">
<head>
<meta charset="utf-8">
<title>Marlow Vantage — Livre blanc RGPD et Cyberattaques</title>
<link rel="stylesheet" href="https://fonts.googleapis.com/css2?family=Montserrat:wght@800;900&family=Open+Sans:wght@400;600;700&display=swap">
<style>
:root{
  --board:#1b1b1c;
  --paper:#ffffff;
  --cyan:#0bb7e2;
  --cyan-soft:#bfeaf6;
  --green:#b9d24a;
  --mist:#ececec;
  --ink:#2b2b2b;
  --body:#3c3c3c;
  --link:#1a2fb8;
}
*{margin:0;padding:0;box-sizing:border-box}
html,body{width:758px;height:1200px;overflow:hidden;background:var(--board)}
.board{position:relative;width:758px;height:1200px;background:var(--board)}
.page{position:absolute;width:273px;height:353px;background:var(--paper);overflow:hidden;font-family:"Open Sans",sans-serif;color:var(--body)}
.page-cover{left:388px;top:55px}
.page-intro{left:97px;top:421px}
.page-context{left:388px;top:421px}
.page-action{left:388px;top:793px}

.page-wash{position:absolute;inset:0;background:linear-gradient(180deg,#ffffff 0%,#ffffff 58%,var(--mist) 70%,var(--cyan-soft) 80%,var(--cyan) 90%,var(--green) 100%)}
.page-band{position:absolute;left:0;right:0;bottom:0;height:46px;background:var(--cyan);border-radius:60% 60% 0 0 / 30px 30px 0 0}

.brand{position:absolute;display:flex;align-items:center;gap:3px;font-family:"Open Sans",sans-serif;font-weight:700;color:var(--cyan);line-height:1.05;text-transform:uppercase}
.brand-dot{width:9px;height:9px;border-radius:50%;background:var(--cyan);flex:none}
.brand-cover{right:26px;top:36px;font-size:8px}
.brand-cover .brand-dot{width:12px;height:12px}
.brand-inner{left:11px;top:28px;font-size:5.6px}
.brand-inner .brand-dot{width:7px;height:7px}

.cover-title{position:absolute;left:65px;top:129px;font-family:"Montserrat",sans-serif;font-weight:800;font-size:12.8px;line-height:19px;color:var(--ink)}
.cover-url{position:absolute;right:22px;top:323px;font-family:"Open Sans",sans-serif;font-weight:700;font-size:5.4px;color:var(--ink)}

.intro-title{position:absolute;left:79px;top:84px;width:180px;font-family:"Montserrat",sans-serif;font-weight:900;font-size:9.6px;line-height:12.8px;color:var(--cyan)}
.intro-lead{position:absolute;left:79px;top:137px;width:148px;font-weight:700;font-size:5.1px;line-height:7.3px;color:var(--ink)}
.intro-lead p+p{margin-top:7px}

.footer{position:absolute;right:0;bottom:0;height:28px;display:flex;align-items:flex-start}
.footer-title{margin-top:7px;text-align:right;font-family:"Montserrat",sans-serif;font-weight:800;font-size:3.3px;line-height:4.1px;color:var(--ink)}
.footer-rule{width:.6px;height:28px;background:var(--ink);margin:0 8px 0 4px}
.footer-num{margin-top:8px;width:16px;font-family:"Montserrat",sans-serif;font-weight:800;font-size:5px;color:var(--ink)}

.copy{position:absolute;left:57px;top:34px;width:193px;font-size:5.1px;line-height:7.35px}
.copy p{margin-bottom:5px}
.dash-list{list-style:none;margin:0 0 12px 7px}
.dash-list li{position:relative;padding-left:10px;margin-bottom:5px}
.dash-list li::before{content:"-";position:absolute;left:0}
.num-list{margin:0 0 6px 16px;padding-left:0}
.num-list li{padding-left:5px;margin-bottom:5px}
.zero-list{list-style:none;margin:0 0 5px 6px}
.zero-list li{display:flex;gap:6px;margin-bottom:1.5px}
.zero-list span{width:6px}
.action-kicker{font-family:"Montserrat",sans-serif;font-weight:900;font-size:6.6px;color:var(--cyan);margin-bottom:9px}
.action-title{font-weight:700;font-size:5.9px;line-height:8px;color:var(--cyan);margin-bottom:16px}
.copy a{color:var(--link);text-decoration:underline}
.page-action .copy{top:36px;height:284px;overflow:hidden}
</style>
</head>
<body>
<main class="board">

  <section class="page page-cover" aria-label="Couverture">
    <div class="page-wash" role="img" aria-label="Fond décoratif en dégradé blanc, gris clair, bleu et vert"></div>
    <div class="brand brand-cover"><span class="brand-dot"></span><span>Marlow<br>Vantage</span></div>
    <h1 class="cover-title">RGPD et Cyberattaques<br>4 actions pour assurer<br>et rassurer</h1>
    <p class="cover-url">www.marlow-vantage.net</p>
  </section>

  <section class="page page-intro" aria-label="Page 2">
    <div class="page-wash" role="img" aria-label="Fond décoratif en dégradé blanc, gris clair, bleu et vert"></div>
    <div class="brand brand-inner"><span class="brand-dot"></span><span>Marlow<br>Vantage</span></div>
    <h2 class="intro-title">Modèle de maturité<br>ARPN et Cyberattaques:<br>4 actions pour rassurer</h2>
    <div class="intro-lead">
      <p>Initier une nouvelle auto-évaluation avec le modèle de maturité publié par la ARPN le 9 septembre 2021</p>
      <p>En quelques mois, à cause et grâce au Covid, le marché a gagné en maturité et en expérience, ce qui a conduit les acteurs de la conformité et les régulateurs, dont la ARPN avec son modèle de maturité publié le 9 septembre 2021, à mettre à disposition des organisations, des outils qui permettent aux organisations d'engager des actions concrètes et pragmatiques leur permettant de faire face.</p>
    </div>
    <footer class="footer"><p class="footer-title">RGPD et Cyberattaques 4 actions<br>pour assurer et rassurer</p><span class="footer-rule"></span><span class="footer-num">2</span></footer>
  </section>

  <section class="page page-context" aria-label="Page 3">
    <div class="page-band" aria-hidden="true"></div>
    <div class="brand brand-inner"><span class="brand-dot"></span><span>Marlow<br>Vantage</span></div>
    <div class="copy">
      <p>Dans ce contexte, plusieurs constats permettent de comprendre l'urgence d'agir :</p>
      <ul class="dash-list">
        <li>Depuis le Covid, les services d'audit interne multiplient leurs interventions et déplorent que les entreprises sous-traitantes ne respectent pas la réglementation et ne disposent pas de mesures de sécurité susceptibles de protéger leurs clients.</li>
        <li>La concurrence entre entreprises sous-traitantes n'a jamais été aussi tendue, ce qui autorise les acheteurs à augmenter leur niveau d'exigence en imposant des demandes qui paraissaient déraisonnables il y a encore quelques mois.</li>
        <li>Bon nombre de sinistres cybers analysés par les compagnies d'assurances ont fait apparaître des lacunes en matière de conformité et de sécurité qu'elles refusent désormais de couvrir.</li>
      </ul>
      <p>Nous avons identifié ainsi quatre actions prioritaires pour assurer et rassurer efficacement clients, utilisateurs et investisseurs :</p>
      <ol class="num-list">
        <li>Initier une nouvelle auto-évaluation avec le modèle de maturité publié par la ARPN le 9 septembre 2021</li>
        <li>Mettre en place des indicateurs objectifs en matière de sécurité, en s'appuyant sur des outils qui permettent de disposer d'une notation sécurité par une tierce partie et notamment des outils tels que TrustGaugeo ou Notavio.</li>
        <li>Mettre en place et faire vivre un dossier de conformité solide adapté aux spécificités de l'entreprise, incluant les 61 mesures du modèle de la ARPN dont on extraira les éléments clés pour mettre à la disposition des équipes commerciales une base de connaissance les aidant à répondre aux clients et aux prospects et ainsi ne pas perdre de marchés.</li>
        <li>Mixer des compétences internes (savoir-faire métier) et externes (expertise RGPD, cybersécurité) pour garantir une réelle expertise (capacité à se protéger et protéger ses partenaires contre les attaques malveillantes) et être capable de faire face à la variabilité de la demande.</li>
      </ol>
    </div>
    <footer class="footer"><p class="footer-title">RGPD et Cyberattaques 4 actions<br>pour assurer et rassurer</p><span class="footer-rule"></span><span class="footer-num">3</span></footer>
  </section>

  <section class="page page-action" aria-label="Page 4">
    <div class="page-band" aria-hidden="true"></div>
    <div class="brand brand-inner"><span class="brand-dot"></span><span>Marlow<br>Vantage</span></div>
    <div class="copy">
      <h3 class="action-kicker">Première action :</h3>
      <p class="action-title">Initier une nouvelle auto-évaluation avec le modèle de maturité publié par la ARPN le 9 septembre 2021</p>
      <p>Le 9 septembre 2021, la ARPN a partagé ses premières réflexions sur la réalisation d'un modèle de maturité en gestion de la protection des données et a mis en ligne sur son site une '<a>première version de son modèle d'autoévaluation. Le projet de modèle décrit « 8 activités types liées à la protection des données en 5 niveaux de maturité ».</a></p>
      <p>Nous avons testé ce modèle, dénommé “méthode de maturité” auprès de différentes entreprises clientes. Les retours des dirigeants opérationnels sont étonnamment positifs compte tenu du caractère réglementaire austère de la conformité RGPD. Ce modèle est un bel exemple de que peut produire l'intelligence juridique, puisqu'il va non seulement permettre aux Directions Juridiques et aux Délégués à la Protection des Données (DPO) de structurer les Dossiers de Conformité, mais aussi de sécuriser et d'éclairer les stratégies et les prises de décision. La méthode propose six niveaux de maturité de manière générique :</p>
      <ul class="zero-list">
        <li><span>0.</span>Pratique inexistante ou incomplète</li>
        <li><span>1.</span>Pratique informelle (quelques actions isolées)</li>
        <li><span>2.</span>Pratique répétable et suivie (des actions reproductibles)</li>
        <li><span>3.</span>Processus défini (standardisation des pratiques)</li>
        <li><span>4.</span>Processus contrôlé (mesure quantitative et correction des défauts)</li>
        <li><span>5.</span>Processus continuellement optimisé (amélioration continue)</li>
      </ul>
      <p>Chaque niveau évalue la manière dont un organisme conçoit, met en œuvre, contrôle, maintient et assure le suivi d'une activité, quel que soit cette activité. L'atteinte d'un niveau supérieur suppose d'avoir déjà atteint le niveau précédent.</p>
      <p>Si le niveau 3 peut être facilement atteint, les niveaux supérieurs vont nécessiter implication et récurrence des actions.</p>
      <p>Pour mieux appréhender l'intérêt opérationnel de ce modèle, nous avons réalisé une évaluation de maturité avec les responsables de traitement de</p>
    </div>
    <footer class="footer"><p class="footer-title">RGPD et Cyberattaques 4 actions<br>pour assurer et rassurer</p><span class="footer-rule"></span><span class="footer-num">4</span></footer>
  </section>

</main>
</body>
</html>
```